DrivPeak Agile Coaching Website

I need an updated website for www.drivpeak.example. I'm looking for a modern look. This is a professional site, but I don't want it to look "stuffy". It needs to have an element of fun and learning.

My services include:
Lean Agile Coaching
Lean Agile Training
Facilitation
Workshops
Consulting

Ideas this site should convey: collaboration, learning, teamwork, adaptability, flow, limited WIP, agility, Lean.

I would like to use some of my own photos and slide decks for content: http://www.deckvault.example/mornbeck/presentations

I would also like to include the Peerlinko recommendations I have from customers: https://www.peerlinko.example/in/mornbeck

Examples of sites I like:
http://www.quarrelmosswidget.example
http://www.forthsprintly.example

Target Market(s)

IT professionals, software development managers

Industry/Entity Type

It Company

Coding

Coded - Design and coding required

Font styles to use
Serif
Sans Serif

Requirements
Must have
• Original looking graphics and layout.
• My logo must be included in layout.
• Need to feature my blog content.
• Deliverable must be a WordPress theme that I can install.
• Responsive site.
Nice to have
• Use images from my slides on Deckvault if they make sense.

```html
<!DOCTYPE html>
<html lang="en">
<head>
<meta charset="utf-8">
<title>DrivPeak — Lean Agile Coaching</title>
<link rel="stylesheet" href="https://fonts.googleapis.com/css2?family=Bebas+Neue&family=Open+Sans:wght@400;600&family=Roboto+Condensed:wght@400;700&display=swap">
<style>
:root{
  --green:#0acb3a;
  --green-dark:#08b232;
  --ink:#111;
  --text:#555;
  --muted:#8a8a8a;
  --panel:#ececec;
  --line:#cfcfcf;
  --white:#fff;
  --black:#000;
  --topbar:#eceef1;
}
*{box-sizing:border-box;margin:0;padding:0}
html,body{width:1200px;height:2894px;overflow:hidden}
body{position:relative;background:var(--white);font-family:"Open Sans",Arial,sans-serif;color:var(--text)}
.abs{position:absolute}
.cond{font-family:"Roboto Condensed","Arial Narrow",sans-serif}

/* top bar */
.topbar{left:0;top:0;width:1200px;height:42px;background:var(--topbar)}
.social-mini{top:12px;width:18px;height:18px;border-radius:50%}
.search{left:874px;top:6px;width:249px;height:31px;border:1px solid #cfd2d6;background:#fff}
.search span{position:absolute;left:10px;top:6px;font-size:14px;color:#999}
.search-btn{left:1090px;top:6px;width:33px;height:31px;background:#c7c9cc}

/* header */
.brand{left:77px;top:50px;font-family:"Roboto Condensed",sans-serif;font-weight:700;font-size:62px;color:var(--ink);letter-spacing:-1px;line-height:70px}
.brand-mark{left:77px;top:54px;width:14px;height:62px;background:var(--green)}
.nav a{position:absolute;top:58px;height:50px;line-height:50px;font-family:"Roboto Condensed",sans-serif;font-size:18px;color:#888;text-decoration:none;text-align:center}
.nav .active{left:642px;width:114px;background:var(--green);color:#fff}

/* hero */
.hero{left:0;top:125px;width:1200px;height:573px;background:linear-gradient(120deg,#6b5a48 0%,#8f877c 30%,#d4d0c8 50%,#5c6670 75%,#2e3338 100%)}
.hero-band{left:0;top:355px;width:1200px;height:108px;background:rgba(20,20,20,.55)}
.hero-title{left:0;top:350px;width:1200px;text-align:center;font-family:"Bebas Neue",sans-serif;font-size:66px;color:#fff;letter-spacing:1px}
.hero-sub{left:0;top:428px;width:1200px;text-align:center;font-size:23px;color:#fff}
.btn{background:var(--green);color:#fff;font-family:"Roboto Condensed",sans-serif;text-align:center;text-transform:uppercase}
.hero-btn{left:503px;top:494px;width:193px;height:50px;line-height:50px;font-size:18px}

/* services */
.services{left:0;top:698px;width:1200px;height:645px;background:var(--panel)}
.svc-icon{width:124px;height:124px;border-radius:50%;background:#fff;display:flex;align-items:center;justify-content:center}
.svc-title{width:320px;text-align:center;font-family:"Roboto Condensed",sans-serif;font-size:24px;color:var(--green)}
.svc-text{width:320px;text-align:center;font-size:14.5px;line-height:25px;color:var(--muted)}

/* welcome */
.welcome-h{left:77px;top:1420px;font-family:"Roboto Condensed",sans-serif;font-size:46px;color:var(--ink)}
.welcome-h span,.sec-h span{color:var(--green)}
.welcome-p{left:77px;top:1495px;width:590px;font-size:15.5px;line-height:25px;color:#444}
.welcome-btn{left:77px;top:1628px;width:166px;height:50px;line-height:50px;font-size:19px}
.welcome-logo{left:696px;top:1431px;width:427px;height:218px;background:radial-gradient(ellipse at center,#fff 0%,#f0f0f0 55%,#dcdcdc 100%);display:flex;align-items:center;justify-content:center}
.welcome-logo span{font-family:"Roboto Condensed",sans-serif;font-weight:700;font-size:80px;color:var(--ink);letter-spacing:-1px}

/* blog + testimonials */
.band{left:0;top:1732px;width:1200px;height:434px;background:var(--panel)}
.sec-h{font-family:"Roboto Condensed",sans-serif;font-size:46px;color:var(--ink)}
.rule{height:1px;background:var(--line)}
.thumb{width:156px;border:1px solid #d5d5d5}
.post-title{font-size:15px;color:var(--green)}
.post-date{font-size:15px;color:#666}
.post-text{width:320px;font-size:15px;line-height:23px;color:#555}
.post-text a{color:var(--green);text-decoration:underline}
.arrow{width:38px;height:38px;border-radius:50%;border:1px solid var(--green);display:flex;align-items:center;justify-content:center}
.avatar{left:830px;top:1881px;width:92px;height:92px;border-radius:50%;border:2px solid #fff;background:linear-gradient(#6a4a3a,#c9a58f);box-shadow:0 0 0 1px #ccc}
.quote{left:652px;top:2004px;width:442px;text-align:center;font-size:15px;line-height:23px;color:#555}
.client{left:652px;top:2070px;width:442px;text-align:center;font-size:18px;color:var(--green)}

/* contact */
.field{background:var(--panel);font-size:14px;color:#999;padding:14px 20px}
.field.name{background:#fff;border:1px solid #ccc}
.submit{left:459px;top:2425px;width:625px;height:50px;line-height:50px;font-size:21px}

/* footer */
.footer{left:0;top:2527px;width:1200px;height:312px;background:var(--black)}
.foot-logo{left:77px;top:2570px;font-family:"Roboto Condensed",sans-serif;font-weight:700;font-size:50px;color:#fff;letter-spacing:-1px}
.foot-about{left:79px;top:2662px;width:230px;font-size:15px;line-height:25px;color:#fff}
.foot-h{top:2570px;font-family:"Roboto Condensed",sans-serif;font-size:22px;color:var(--green)}
.foot-link{left:349px;font-size:14px;color:#fff}
.foot-input{left:619px;width:234px;height:37px;border:2px solid #fff;font-size:14px;color:#fff;padding:7px 6px}
.subscribe{left:619px;top:2749px;width:145px;height:40px;line-height:40px;background:#fff;color:#000;font-family:"Roboto Condensed",sans-serif;font-size:19px;text-align:center}
.touch{left:891px;font-size:15px;line-height:25px;color:#fff}
.touch svg{vertical-align:-3px;margin-right:10px}
.foot-social{width:54px;height:54px;border-radius:50%;background:#fff}
.foot-social.dim{background:#9a9a9a}
.bottom{left:0;top:2839px;width:1200px;height:55px;background:var(--green);text-align:center;line-height:55px;font-size:15px;color:#fff}
</style>
</head>
<body>

<!-- top bar -->
<div class="abs topbar"></div>
<div class="abs social-mini" style="left:70px;background:var(--green)"></div>
<div class="abs social-mini" style="left:120px;background:#444"></div>
<div class="abs social-mini" style="left:173px;background:#444"></div>
<div class="abs social-mini" style="left:223px;background:#444"></div>
<div class="abs search"><span>Search here...</span></div>
<div class="abs search-btn"><svg width="33" height="31" viewBox="0 0 33 31"><circle cx="15" cy="14" r="6" fill="none" stroke="#fff" stroke-width="2.5"/><line x1="19.5" y1="18.5" x2="24" y2="23" stroke="#fff" stroke-width="2.5"/></svg></div>

<!-- header -->
<div class="abs brand-mark"></div>
<div class="abs brand" style="left:98px">DrivPeak</div>
<nav class="nav">
  <a class="active" href="#">HOME</a>
  <a href="#" style="left:776px;width:80px">ABOUT</a>
  <a href="#" style="left:895px;width:100px">SERVICES</a>
  <a href="#" style="left:1040px;width:92px">CONTACT</a>
</nav>

<!-- hero -->
<div class="abs hero" role="img" aria-label="Photo of a team collaborating around a desk with laptops, charts and coffee"></div>
<div class="abs hero-band"></div>
<div class="abs hero-title">"Clarity, Understanding, Improvement"</div>
<div class="abs hero-sub">Improving software development through alignment, visibility, knowledge and discipline.</div>
<div class="abs btn hero-btn">Contact us now</div>

<!-- services -->
<section class="abs services"></section>

<div class="abs svc-icon" style="left:171px;top:748px">
  <svg width="64" height="64" viewBox="0 0 64 64" fill="var(--green)"><path d="M8 26h10l26-14v40L18 38H8z"/><rect x="14" y="38" width="8" height="14" rx="2"/><path d="M50 22l8-5M50 32h9M50 42l8 5" stroke="var(--green)" stroke-width="3" fill="none"/></svg>
</div>
<div class="abs svc-title" style="left:73px;top:882px">Lean Agile Coaching</div>
<div class="abs svc-text" style="left:73px;top:924px">Lorem Ipsum is simply dummy text of the printing and typesetting industry. Lorem Ipsum has been the industry.</div>

<div class="abs svc-icon" style="left:538px;top:748px">
  <svg width="64" height="64" viewBox="0 0 64 64" fill="var(--green)"><circle cx="16" cy="12" r="6"/><path d="M9 22h14l8 6-3 3-5-3v28h-5V40h-2v16H11V28H9z"/><rect x="30" y="10" width="28" height="24" fill="none" stroke="var(--green)" stroke-width="3"/><path d="M36 28l6-8 5 5 6-9" stroke="var(--green)" stroke-width="2.5" fill="none"/><line x1="44" y1="34" x2="44" y2="44" stroke="var(--green)" stroke-width="3"/></svg>
</div>
<div class="abs svc-title" style="left:440px;top:882px">Lean Agile Training</div>
<div class="abs svc-text" style="left:440px;top:924px">Lorem Ipsum is simply dummy text of the printing and typesetting industry. Lorem Ipsum has been the industry.</div>

<div class="abs svc-icon" style="left:904px;top:748px">
  <svg width="64" height="64" viewBox="0 0 64 64"><g stroke="var(--green)" stroke-width="6" stroke-linecap="round"><line x1="12" y1="12" x2="52" y2="52"/><line x1="52" y1="12" x2="12" y2="52"/></g><g stroke="#fff" stroke-width="1.5"><line x1="20" y1="16" x2="16" y2="20"/><line x1="28" y1="24" x2="24" y2="28"/><line x1="36" y1="32" x2="32" y2="36"/></g></svg>
</div>
<div class="abs svc-title" style="left:806px;top:882px">Facilitation</div>
<div class="abs svc-text" style="left:806px;top:924px">Lorem Ipsum is simply dummy text of the printing and typesetting industry. Lorem Ipsum has been the industry.</div>

<div class="abs svc-icon" style="left:351px;top:1045px">
  <svg width="64" height="64" viewBox="0 0 64 64" fill="var(--green)"><rect x="28" y="6" width="28" height="20" fill="none" stroke="var(--green)" stroke-width="3"/><path d="M33 21l6-7 5 4 6-7" stroke="var(--green)" stroke-width="2.5" fill="none"/><circle cx="16" cy="18" r="5"/><path d="M9 27h14l8 4-2 3-6-2v10H10z"/><circle cx="12" cy="44" r="5"/><circle cx="30" cy="44" r="5"/><circle cx="48" cy="44" r="5"/><path d="M4 58c0-6 4-8 8-8s8 2 8 8zM22 58c0-6 4-8 8-8s8 2 8 8zM40 58c0-6 4-8 8-8s8 2 8 8z"/></svg>
</div>
<div class="abs svc-title" style="left:253px;top:1179px">Workshops</div>
<div class="abs svc-text" style="left:253px;top:1221px">Lorem Ipsum is simply dummy text of the printing and typesetting industry. Lorem Ipsum has been the industry.</div>

<div class="abs svc-icon" style="left:717px;top:1045px">
  <svg width="64" height="64" viewBox="0 0 64 64" fill="var(--green)"><circle cx="20" cy="12" r="5"/><circle cx="44" cy="12" r="5"/><path d="M13 20h14v12H13zM37 20h14v12H37z"/><rect x="6" y="30" width="52" height="6"/><circle cx="20" cy="44" r="5"/><circle cx="44" cy="44" r="5"/><path d="M13 52h14v8H13zM37 52h14v8H37z"/><rect x="6" y="34" width="4" height="24"/><rect x="54" y="34" width="4" height="24"/></svg>
</div>
<div class="abs svc-title" style="left:619px;top:1179px">Consulting</div>
<div class="abs svc-text" style="left:619px;top:1221px">Lorem Ipsum is simply dummy text of the printing and typesetting industry. Lorem Ipsum has been the industry.</div>

<!-- welcome -->
<h1 class="abs welcome-h" style="font-weight:400">WELCOME TO <span>DRIVPEAK</span></h1>
<p class="abs welcome-p">DrivPeak is a company dedicated to improving the art and science of software development for both the consumers of software services and the professionals doing the work. Our primary focus is the marketplace and community where we live–the Kansas City metro area.</p>
<div class="abs btn welcome-btn">Read more</div>
<div class="abs welcome-logo"><span>DrivPeak</span></div>

<!-- blog + testimonials -->
<section class="abs band"></section>
<h2 class="abs sec-h" style="left:77px;width:517px;top:1776px;text-align:center;font-weight:400"><span>BLOG</span></h2>
<div class="abs rule" style="left:77px;top:1846px;width:517px"></div>

<div class="abs thumb" style="left:77px;top:1877px;height:104px;background:linear-gradient(#f4f8fb,#dde9f1)" role="img" aria-label="Conference announcement slide"></div>
<div class="abs post-title" style="left:262px;top:1873px">Speaking at FlowConf 2016</div>
<div class="abs post-date" style="left:262px;top:1900px"><svg width="13" height="13" viewBox="0 0 13 13" style="vertical-align:-1px;margin-right:6px"><rect x="1" y="2" width="11" height="10" fill="none" stroke="#666" stroke-width="1.5"/><line x1="1" y1="5" x2="12" y2="5" stroke="#666" stroke-width="1.5"/></svg>October 4, 2016</div>
<div class="abs post-text" style="left:262px;top:1929px">I'm pleased to announce I'll be speaking at FlowConf 2016 in Atlanta...&nbsp;&nbsp; <a>READ MORE</a></div>

<div class="abs thumb" style="left:77px;top:2010px;height:106px;background:linear-gradient(#fbfbf6,#e4e6dc)" role="img" aria-label="Talk title slide with presentation preview"></div>
<div class="abs post-title" style="left:262px;top:2007px">MWDC 2015 Minimum Viable Agile Talk</div>
<div class="abs post-date" style="left:262px;top:2034px"><svg width="13" height="13" viewBox="0 0 13 13" style="vertical-align:-1px;margin-right:6px"><rect x="1" y="2" width="11" height="10" fill="none" stroke="#666" stroke-width="1.5"/><line x1="1" y1="5" x2="12" y2="5" stroke="#666" stroke-width="1.5"/></svg>October 4, 2016</div>
<div class="abs post-text" style="left:262px;top:2063px">I gave a talk on Minimum Viable Agile at MWDC 2015. The theme is to...&nbsp;&nbsp; <a>READ MORE</a></div>

<h2 class="abs sec-h" style="left:652px;top:1776px;font-weight:400">WHAT OUR <span>CLIENT SAY</span></h2>
<div class="abs rule" style="left:652px;top:1846px;width:442px"></div>
<div class="abs arrow" style="left:675px;top:1910px"><svg width="12" height="16" viewBox="0 0 12 16"><path d="M9 2L3 8l6 6" stroke="var(--green)" stroke-width="1.8" fill="none"/></svg></div>
<div class="abs arrow" style="left:1032px;top:1910px"><svg width="12" height="16" viewBox="0 0 12 16"><path d="M3 2l6 6-6 6" stroke="var(--green)" stroke-width="1.8" fill="none"/></svg></div>
<div class="abs avatar" role="img" aria-label="Client portrait"></div>
<p class="abs quote">Brant's breadth of experiences and knowledge provides him the insight to quickly understand organizational...</p>
<div class="abs client">-CLIENT NAME</div>

<!-- contact -->
<h2 class="abs sec-h" style="left:0;width:1200px;top:2210px;text-align:center;font-weight:400">CONTACT <span>US</span></h2>
<div class="abs field name" style="left:116px;top:2299px;width:333px;height:51px">Name</div>
<div class="abs field" style="left:116px;top:2361px;width:333px;height:52px">E - Mail</div>
<div class="abs field" style="left:116px;top:2425px;width:333px;height:50px">Phone</div>
<div class="abs field" style="left:459px;top:2299px;width:625px;height:114px">Message</div>
<div class="abs btn submit">Submit</div>

<!-- footer -->
<footer class="abs footer"></footer>
<div class="abs foot-logo">DrivPeak</div>
<p class="abs foot-about">Improving software development through alignment, visibility, knowledge, and discipline.</p>

<div class="abs foot-h" style="left:349px">Useful links</div>
<div class="abs foot-link" style="top:2621px">Home</div>
<div class="abs foot-link" style="top:2652px">About</div>
<div class="abs foot-link" style="top:2683px">Services</div>
<div class="abs foot-link" style="top:2716px">Contact</div>

<div class="abs foot-h" style="left:619px">Newsletter</div>
<div class="abs foot-input" style="top:2621px">Enter Name</div>
<div class="abs foot-input" style="top:2685px">Enter Email</div>
<div class="abs subscribe">SUBSCRIBE</div>

<div class="abs foot-h" style="left:891px">Get In Touch With Us</div>
<div class="abs touch" style="top:2618px;width:240px;padding-left:28px;text-indent:-28px"><svg width="16" height="18" viewBox="0 0 16 18"><path d="M8 1a6 6 0 0 0-6 6c0 5 6 10 6 10s6-5 6-10a6 6 0 0 0-6-6z" fill="#fff"/><circle cx="8" cy="7" r="2.2" fill="#000"/></svg>Lorem Ipsum is simply dummy text.</div>
<div class="abs touch" style="top:2682px"><svg width="16" height="16" viewBox="0 0 16 16"><path d="M3 1l3 3-2 2c1 2 4 5 6 6l2-2 3 3-2 2C8 15 1 8 1 3z" fill="#fff"/></svg>Lorem Ipsum is simply</div>
<div class="abs touch" style="top:2719px"><svg width="18" height="14" viewBox="0 0 18 14"><rect x="1" y="1" width="16" height="12" fill="none" stroke="#fff" stroke-width="1.6"/><path d="M1 2l8 6 8-6" stroke="#fff" stroke-width="1.6" fill="none"/></svg>info@drivpeak.example</div>
<div class="abs foot-social" style="left:889px;top:2757px"></div>
<div class="abs foot-social dim" style="left:961px;top:2757px"></div>
<div class="abs foot-social dim" style="left:1034px;top:2757px"></div>

<div class="abs bottom">© <b>DRIVPEAK</b> - 2016. All Rights Reserved.</div>

</body>
</html>
```